New Fun, Positive, energised looking Business Card Needed for High Achiever Coach

I am looking for a two sided full colour business card. I am self employed and have recently re branded my 1-2-1 work re-vitalising high achievers. My target client base for these cards is therefore high achievers - usually aged 40 -55, they are often entrepreneurs, CEO or work in banking and finance and 2/3 are male. I work with them on 90 day or 6 month coaching programs to help them live their success in a healthier, more sustainable and fulfiiled way. They pay for this privately so though they are corporate types the cards need not look 'corporate'. I want to portray the idea of transformation, vitality and re-connecting.
You can get a feel for the look I like on my new website: corinvale.co.uk
I want to use this logo with strapline (Re-Vitalising High Achievers) (I purchased off Logoharbor) and font/ colours (the turquoise and green).
Details to include on the card:
www.corinvale.co.uk
+44 7915 264318
mira@corinvale.co.uk
skype: miracorin
I'd also like to include:
Do you struggle to switch off? Want to be healthier and feel fitter? Want closer relationships? More clarity over the direction you are headed? I can help you do these things using integrated mind-body techniques. Visit corinvale.co.uk TODAY to apply for a FREE Breakthrough session.
BUT if that is too much text for a card I am open to advice/ammendments.
Updates
Thanks for your design - I am considering them. PLease change the wording to :

```html
<!DOCTYPE html>
<html lang="en">
<head>
<meta charset="utf-8">
<title>Mira Corin – Business Card</title>
<link rel="stylesheet" href="https://fonts.googleapis.com/css2?family=Alfa+Slab+One&family=Arimo:wght@400;700&family=Dancing+Script:wght@500&display=swap">
<style>
  :root {
    --stage: #646467;
    --paper: #ffffff;
    --paper-back: #f1f1f3;
    --turquoise: #0aa6cf;
    --green: #5cb85f;
    --faint: #dbe6ec;
    --white: #ffffff;
  }
  * { box-sizing: border-box; margin: 0; padding: 0; }
  html, body {
    width: 1035px; height: 1200px; overflow: hidden;
    background: var(--stage);
  }
  .canvas { position: relative; width: 1035px; height: 1200px; }

  .card { position: absolute; overflow: hidden; }
  .card--front { left: 51px; top: 33px; width: 950px; height: 543px; background: var(--paper); }
  .card--back  { left: 42px; top: 618px; width: 951px; height: 546px; background: var(--paper-back); }

  .front-wave { position: absolute; inset: 0; width: 100%; height: 100%; }

  .brand { position: absolute; left: 22px; top: 100px; width: 460px; text-align: center; }
  .brand__mark {
    display: block; width: 132px; height: 132px; margin: 0 auto 42px;
    border-radius: 50%; background: var(--green);
  }
  .brand__name {
    font-family: "Alfa Slab One", serif; font-weight: 400;
    font-size: 48px; line-height: 1; color: var(--turquoise); letter-spacing: 1px;
  }
  .brand__strapline {
    margin-top: 10px;
    font-family: "Dancing Script", cursive; font-weight: 500;
    font-size: 28px; line-height: 1; color: var(--turquoise);
  }

  .contact { position: absolute; left: 566px; top: 196px; list-style: none; }
  .contact__item {
    display: flex; align-items: center; height: 34px;
    font-family: "Arimo", sans-serif; font-size: 25px; color: var(--white);
  }
  .contact__icon { width: 24px; height: 24px; margin-right: 18px; flex: none; }

  .back-decor { position: absolute; left: 0; top: 0; width: 100%; height: 100%; }

  .pitch {
    position: absolute; left: 0; right: 0; top: 356px;
    text-align: center; font-family: "Arimo", sans-serif;
    font-size: 22.5px; line-height: 31px; color: var(--green);
  }
  .pitch__visit { margin-top: 4px; line-height: 34px; }
  .pitch__url { color: var(--turquoise); font-weight: 700; font-size: 26px; }
</style>
</head>
<body>
<main class="canvas">

  <section class="card card--front" aria-label="Card front">
    <svg class="front-wave" viewBox="0 0 950 543" aria-hidden="true">
      <path d="M303 0 C400 40 450 120 468 220 C485 330 520 450 700 543 L950 543 L950 0 Z" fill="var(--turquoise)"/>
      <path d="M510 280 C530 400 600 480 770 543" fill="none" stroke="var(--white)" stroke-width="5" stroke-linecap="round"/>
    </svg>

    <div class="brand">
      <span class="brand__mark"></span>
      <p class="brand__name">Mira Corin</p>
      <p class="brand__strapline">Re-Vitalising High Achievers</p>
    </div>

    <ul class="contact">
      <li class="contact__item">
        <svg class="contact__icon" viewBox="0 0 24 24" aria-hidden="true">
          <path d="M2 8 Q12 1 22 8 L19 11 L16 8 L8 8 L5 11 Z" fill="#fff"/>
          <rect x="5" y="11" width="14" height="9" rx="2" fill="#fff"/>
        </svg>
        +44 7915 264318
      </li>
      <li class="contact__item">
        <svg class="contact__icon" viewBox="0 0 24 24" aria-hidden="true">
          <circle cx="12" cy="12" r="10" fill="#fff"/>
        </svg>
        miracorin
      </li>
      <li class="contact__item">
        <svg class="contact__icon" viewBox="0 0 24 24" aria-hidden="true">
          <circle cx="12" cy="12" r="10" fill="none" stroke="#fff" stroke-width="2"/>
          <ellipse cx="12" cy="12" rx="4" ry="10" fill="none" stroke="#fff" stroke-width="2"/>
          <path d="M2 12 H22" stroke="#fff" stroke-width="2"/>
        </svg>
        www.corinvale.co.uk
      </li>
      <li class="contact__item">
        <svg class="contact__icon" viewBox="0 0 24 24" aria-hidden="true">
          <rect x="2" y="5" width="20" height="14" fill="#fff"/>
          <path d="M2 5 L12 13 L22 5" fill="none" stroke="var(--turquoise)" stroke-width="1.6"/>
        </svg>
        mira@corinvale.co.uk
      </li>
    </ul>
  </section>

  <section class="card card--back" aria-label="Card back">
    <svg class="back-decor" viewBox="0 0 951 546" aria-hidden="true">
      <circle cx="478" cy="210" r="165" fill="none" stroke="var(--faint)" stroke-width="34"/>
    </svg>

    <div class="pitch">
      <p>Do you struggle to switch off? Want to be healthier and feel fitter? Want closer<br>
      relationships? More clarity over the direction you are headed? I can help you do<br>
      these things using integrated mind-body techniques.</p>
      <p class="pitch__visit">Visit <span class="pitch__url">corinvale.co.uk</span></p>
      <p>TODAY to apply for a FREE Breakthrough session.</p>
    </div>
  </section>

</main>
</body>
</html>
```